Business card design for a dynamic IT consulting company

We need a business card design for a young firm, specialized in the Telecommunications/Consulting industry. The name of the company is Brask and Partners Business Consulting Ltd. (Short name: Brask and Partnes)
Brask = solve read reverse, so we aim to be uncomplicated and solution-oriented. The small pipe in our logo is also related to the word solve. So we need a new business card design, which is simple, eye catching and something non traditional (I would probably prefer a square shaped design rather than a rectangle, but open for suggestions). Attached our logo.

Target Market(s)

Usually our customers are Tier1 Telecoms providers (Q-Linkra, Parnexo, etc) and their executives.

Industry/Entity Type

Business

Contact Information for Business Card

Name: Gergely Halmindo
Email: g.halmindo@braskpartnera.hu
Web: www.braskpartnera.hu
Mobile: +36 30 555 0192
Title: Managing Director

Optional:
Company name: Brask and Partners Ltd.
Address: 1047 Budapest, Ravaszi str. 17/B, Hungary

Font styles to use
Other font styles liked:
• helveticaneue_medium, Prime Regular are used now.

Colors

Designer to choose colors to be used in the design.

Requirements
Must have
• I would like to have a 2 sided design.
Nice to have
• I thought if we make the logo a bit bigger (without the company name), that could go to the back with the company name below. I though, if the pipe in the logo is somehow touchable on the business card, would be nice and unique.

```html
<!DOCTYPE html>
<html lang="en">
<head>
<meta charset="utf-8">
<title>Brask &amp; Partners – Business Card</title>
<link rel="stylesheet" href="https://fonts.googleapis.com/css2?family=Exo+2:wght@400;500&family=Arimo:wght@400&display=swap">
<style>
  :root {
    --brand-blue: #1a9ad9;
    --brand-magenta: #b92e96;
    --brand-grey: #5f6165;
    --ink: #3a3b3e;
    --paper: #ffffff;
    --backdrop: #e9e9eb;
  }
  * { margin: 0; padding: 0; box-sizing: border-box; }
  html, body { width: 1200px; height: 1200px; overflow: hidden; }
  body {
    background: var(--backdrop);
    display: flex;
    flex-direction: column;
    align-items: center;
    justify-content: center;
    gap: 60px;
    font-family: "Arimo", Arial, sans-serif;
  }
  .card {
    position: relative;
    width: 820px;
    height: 469px;
    overflow: hidden;
    box-shadow: 0 6px 20px rgba(0,0,0,0.15);
  }

  /* Front side */
  .card--front {
    background: var(--brand-blue);
    color: var(--paper);
    display: flex;
    flex-direction: column;
    align-items: center;
    justify-content: center;
    text-align: center;
  }
  .front__wordmark {
    font-family: "Exo 2", sans-serif;
    font-weight: 500;
    font-size: 68px;
    letter-spacing: 1px;
    line-height: 1;
    margin-bottom: 44px;
  }
  .front__company {
    font-size: 20px;
    letter-spacing: 0.5px;
    margin-bottom: 14px;
  }
  .front__address { font-size: 20px; }

  /* Back side */
  .card--back { background: var(--paper); }
  .back__brand {
    position: absolute;
    left: 56px;
    top: 214px;
    display: flex;
    align-items: center;
    gap: 12px;
  }
  .brand__square {
    width: 28px;
    height: 28px;
    background: var(--brand-blue);
  }
  .brand__name {
    font-family: "Exo 2", sans-serif;
    font-weight: 500;
    font-size: 38px;
    color: var(--brand-grey);
    line-height: 1;
    white-space: nowrap;
  }
  .back__divider {
    position: absolute;
    left: 448px;
    top: 118px;
    width: 1px;
    height: 200px;
    background: var(--brand-blue);
  }
  .back__contact {
    position: absolute;
    left: 474px;
    top: 120px;
  }
  .contact__name {
    font-family: "Exo 2", sans-serif;
    font-weight: 400;
    font-size: 36px;
    color: var(--brand-blue);
    line-height: 1.05;
    white-space: nowrap;
  }
  .contact__title {
    font-size: 17px;
    color: var(--ink);
    margin: 6px 0 18px 2px;
  }
  .contact__list { list-style: none; }
  .contact__item {
    display: flex;
    align-items: center;
    gap: 10px;
    font-size: 16px;
    color: var(--ink);
    margin-bottom: 8px;
    white-space: nowrap;
  }
  .contact__icon { width: 18px; height: 18px; flex: none; }
  .back__stripes {
    position: absolute;
    left: 0;
    bottom: 0;
    width: 820px;
    height: 120px;
  }
</style>
</head>
<body>

  <section class="card card--front" aria-label="Card front">
    <div class="front__wordmark">Brask &amp; Partners</div>
    <p class="front__company">BRASK AND PARTNERS LTD.</p>
    <p class="front__address">1047 Budapest, Ravaszi str. 17/B, Hungary</p>
  </section>

  <section class="card card--back" aria-label="Card back">
    <div class="back__brand">
      <span class="brand__square"></span>
      <span class="brand__name">Brask &amp; Partners</span>
    </div>

    <div class="back__divider"></div>

    <div class="back__contact">
      <h1 class="contact__name">Gergely Halmindo</h1>
      <p class="contact__title">Managing Director</p>
      <ul class="contact__list">
        <li class="contact__item">
          <svg class="contact__icon" viewBox="0 0 18 18" aria-hidden="true">
            <rect x="5" y="1" width="8" height="16" rx="1.5" fill="none" stroke="#1a9ad9" stroke-width="1.6"/>
            <rect x="7" y="3.5" width="4" height="6" fill="#1a9ad9"/>
          </svg>
          +36 30 555 0192
        </li>
        <li class="contact__item">
          <svg class="contact__icon" viewBox="0 0 18 18" aria-hidden="true">
            <circle cx="9" cy="9" r="7.5" fill="none" stroke="#1a9ad9" stroke-width="1.6"/>
            <ellipse cx="9" cy="9" rx="3" ry="7.5" fill="none" stroke="#1a9ad9" stroke-width="1.2"/>
            <line x1="1.5" y1="9" x2="16.5" y2="9" stroke="#1a9ad9" stroke-width="1.2"/>
          </svg>
          www.braskpartnera.hu
        </li>
        <li class="contact__item">
          <svg class="contact__icon" viewBox="0 0 18 18" aria-hidden="true">
            <rect x="1" y="4" width="16" height="11" fill="#1a9ad9"/>
            <polyline points="1,4 9,10.5 17,4" fill="none" stroke="#ffffff" stroke-width="1.3"/>
          </svg>
          g.halmindo@braskpartnera.hu
        </li>
      </ul>
    </div>

    <svg class="back__stripes" viewBox="0 0 820 120" aria-hidden="true">
      <polygon points="0,120 610,120 618,88 0,88" fill="var(--brand-magenta)"/>
      <polygon points="624,120 652,120 668,40 640,40" fill="var(--brand-grey)"/>
      <polygon points="660,120 820,120 820,20 682,20" fill="var(--brand-blue)"/>
    </svg>
  </section>

</body>
</html>
```